Valve bag design

I need a valve bag for 25kg wall putty bag

Here are attached bags for reference

Most of the words or design you can copy from talvuno bag attached and company profile
Also I have attached our local product for reference

```html
<!DOCTYPE html>
<html lang="en">
<head>
<meta charset="utf-8">
<title>Velmora Coat Wall Putty – Valve Bag</title>
<link rel="stylesheet" href="https://fonts.googleapis.com/css2?family=Archivo:wght@400;700;800;900&family=Roboto:wght@400;500;700&display=swap">
<style>
  :root{
    --navy:#253f6e;
    --stone:#b2a7a0;
    --paper:#ffffff;
    --mist:#ece8e6;
    --ink:#111111;
  }
  html,body{margin:0;padding:0;background:var(--paper);overflow:hidden;}
  .canvas{width:1200px;height:685px;overflow:hidden;position:relative;}
  .canvas svg{display:block;width:1200px;height:685px;}
  .face-label{font-family:"Roboto",sans-serif;font-size:44px;fill:var(--ink);}
  .brand{font-family:"Archivo",sans-serif;font-weight:900;letter-spacing:2px;}
  .body{font-family:"Roboto",sans-serif;}
  .bullet{font-family:"Roboto",sans-serif;font-weight:700;fill:var(--navy);font-size:31px;}
  .feature{font-family:"Roboto",sans-serif;font-weight:400;fill:var(--paper);font-size:26px;}
  .back-item{font-family:"Roboto",sans-serif;font-weight:700;fill:var(--navy);font-size:41px;}
  .contact{font-family:"Roboto",sans-serif;font-weight:700;fill:var(--navy);font-size:34px;}
  .star{fill:var(--stone);font-size:24px;font-family:"Roboto",sans-serif;}
</style>
</head>
<body>
<main class="canvas">
<svg viewBox="0 0 2560 1461" xmlns="http://www.w3.org/2000/svg" aria-label="Wall putty valve bag, front and back">
  <text class="face-label" x="648" y="132" text-anchor="middle">FRONT</text>
  <text class="face-label" x="1895" y="132" text-anchor="middle">BACK</text>

  <!-- ===== FRONT FACE ===== -->
  <g class="front-face">
    <rect x="111" y="197" width="1142" height="1141" fill="var(--paper)"/>
    <polygon points="111,197 301,197 301,1085 111,895" fill="var(--stone)"/>
    <polygon points="111,943 301,1133 301,1338 111,1338" fill="var(--navy)"/>
    <text class="brand" transform="translate(148,228) rotate(90)" font-size="44" fill="var(--paper)" textLength="320" lengthAdjust="spacingAndGlyphs">VELMORA COAT</text>
    <text class="brand" x="206" y="1250" text-anchor="middle" font-size="30" fill="var(--paper)">VELMORA</text>

    <polygon points="1063,197 1253,197 1253,590 1063,405" fill="var(--navy)"/>
    <polygon points="1063,450 1253,640 1253,1338 1063,1338" fill="var(--stone)"/>
    <text class="brand" x="1158" y="290" text-anchor="middle" font-size="30" fill="var(--paper)">VELMORA</text>
    <text class="brand" transform="translate(1228,1275) rotate(-90)" font-size="44" fill="var(--paper)" textLength="315" lengthAdjust="spacingAndGlyphs">VELMORA COAT</text>

    <polygon points="301,735 760,735 1045,607 1045,650 775,770 301,770" fill="var(--stone)"/>
    <polygon points="301,787 778,787 1063,660 1063,1338 1008,1338 1008,1270 915,1215 385,1215 301,1133" fill="var(--navy)"/>
    <polygon points="301,1133 385,1215 915,1215 1008,1270 1008,1338 301,1338" fill="var(--stone)"/>

    <text class="body" x="350" y="273" font-size="21" fill="var(--stone)">In Compliance with</text>
    <text class="body" x="350" y="298" font-size="22" font-weight="700" fill="var(--stone)">EN &amp; QBS (Regional)</text>
    <text class="body" x="350" y="323" font-size="21" fill="var(--stone)">Norms</text>

    <text class="brand" x="548" y="388" font-size="42" fill="var(--navy)" textLength="318" lengthAdjust="spacingAndGlyphs">VELMORA COAT</text>

    <g>
      <text class="star" x="358" y="445">★</text><text class="bullet" x="395" y="448">Wall putty</text>
      <text class="star" x="358" y="495">★</text><text class="bullet" x="395" y="498">White base cement putty</text>
      <text class="star" x="358" y="545">★</text><text class="bullet" x="395" y="548">Premium wall putty to use for cement based</text>
      <text class="bullet" x="395" y="599">plaster &amp; concrete surface before paint</text>
      <text class="star" x="358" y="646">★</text><text class="bullet" x="395" y="649">NET WEIGHT 25kg</text>
    </g>

    <circle cx="890" cy="720" r="86" fill="var(--paper)"/>
    <circle cx="890" cy="720" r="72" fill="none" stroke="var(--navy)" stroke-width="3"/>
    <circle cx="890" cy="718" r="44" fill="var(--navy)"/>

    <text class="body" x="363" y="879" font-size="31" font-weight="700" fill="var(--stone)">TOP QUANTIES &amp; FEATURES</text>
    <g>
      <text class="feature" x="400" y="932">➜</text><text class="feature" x="444" y="932">Very smooth and glossy finish</text>
      <text class="feature" x="400" y="970">➜</text><text class="feature" x="444" y="970">Suitable for all cement surfaces</text>
      <text class="feature" x="400" y="1008">➜</text><text class="feature" x="444" y="1008">Suitable for interior &amp; exterior</text>
      <text class="feature" x="400" y="1045">➜</text><text class="feature" x="444" y="1045">Very high tensile adhesion</text>
      <text class="feature" x="400" y="1083">➜</text><text class="feature" x="444" y="1083">Very low water absorption</text>
      <text class="feature" x="400" y="1121">➜</text><text class="feature" x="444" y="1121">No water coming needed</text>
      <text class="feature" x="400" y="1158">➜</text><text class="feature" x="444" y="1158">Very high coverage &amp; easy to apply</text>
    </g>
    <g fill="var(--paper)">
      <rect x="882" y="852" width="50" height="50" rx="7"/>
      <rect x="882" y="917" width="50" height="50" rx="7"/>
      <rect x="882" y="981" width="50" height="50" rx="7"/>
      <rect x="882" y="1046" width="50" height="50" rx="7"/>
      <rect x="882" y="1110" width="50" height="50" rx="7"/>
    </g>

    <text class="body" x="373" y="1287" font-size="25" font-weight="500" fill="var(--navy)">A Premium Product from</text>
    <rect x="676" y="1248" width="3" height="56" fill="var(--navy)"/>
    <text class="brand" x="700" y="1289" font-size="26" fill="var(--navy)">VELMORA COAT</text>
  </g>

  <!-- ===== BACK FACE ===== -->
  <g class="back-face">
    <rect x="1301" y="197" width="1142" height="1141" fill="var(--paper)"/>
    <polygon points="1301,197 1491,197 1491,1085 1301,895" fill="var(--stone)"/>
    <polygon points="1301,943 1491,1133 1491,1338 1301,1338" fill="var(--navy)"/>
    <text class="brand" transform="translate(1338,228) rotate(90)" font-size="44" fill="var(--paper)" textLength="320" lengthAdjust="spacingAndGlyphs">VELMORA COAT</text>
    <text class="brand" x="1396" y="1250" text-anchor="middle" font-size="30" fill="var(--paper)">VELMORA</text>

    <polygon points="2253,197 2443,197 2443,590 2253,405" fill="var(--navy)"/>
    <polygon points="2253,450 2443,640 2443,1338 2253,1338" fill="var(--stone)"/>
    <text class="brand" x="2348" y="290" text-anchor="middle" font-size="30" fill="var(--paper)">VELMORA</text>
    <text class="brand" transform="translate(2418,1275) rotate(-90)" font-size="44" fill="var(--paper)" textLength="315" lengthAdjust="spacingAndGlyphs">VELMORA COAT</text>

    <polygon points="1491,1135 2168,1135 2168,1100 2253,1065 2253,1338 1491,1338" fill="var(--navy)"/>
    <polygon points="2168,1045 2236,1010 2236,1050 2168,1080" fill="var(--stone)"/>
    <rect x="1491" y="1135" width="63" height="40" fill="var(--stone)"/>
    <rect x="1491" y="1175" width="63" height="15" fill="var(--paper)"/>
    <path d="M1554,1100 H2168 V1190 Q2168,1230 2128,1230 H1594 Q1554,1230 1554,1190 Z" fill="var(--paper)"/>

    <text class="brand" x="1593" y="342" font-size="78" fill="var(--stone)" textLength="540" lengthAdjust="spacingAndGlyphs">VELMORA COAT</text>
    <text class="brand" x="1593" y="425" font-size="78" fill="var(--stone)" textLength="485" lengthAdjust="spacingAndGlyphs">WALL PUTTY</text>

    <g>
      <text class="star" x="1588" y="507">★</text><text class="back-item" x="1635" y="511">Application recomentations</text>
      <text class="star" x="1588" y="560">★</text><text class="back-item" x="1635" y="565">Check online</text>
      <text class="star" x="1588" y="614">★</text><text class="back-item" x="1635" y="619">Ask Support</text>
      <text class="star" x="1588" y="668">★</text><text class="back-item" x="1635" y="673">Health and Safety</text>
      <text class="star" x="1588" y="722">★</text><text class="back-item" x="1635" y="727">Product specification</text>
    </g>

    <line x1="1545" y1="792" x2="2195" y2="792" stroke="var(--navy)" stroke-width="2.5" stroke-dasharray="12 9"/>

    <text class="body" x="1542" y="868" font-size="38" font-weight="700" fill="var(--stone)">➜</text>
    <text class="body" x="1596" y="868" font-size="45" font-weight="700" fill="var(--stone)">Market and distributed by :</text>
    <text class="contact" x="1596" y="932">Halbrook Building Ltd</text>
    <text class="contact" x="1596" y="992">TEL : +255700123456</text>
    <text class="contact" x="1596" y="1053">info@halbrookbuilding.com</text>

    <text class="brand" x="1898" y="1192" font-size="30" fill="var(--navy)" textLength="228" lengthAdjust="spacingAndGlyphs">VELMORA COAT</text>
  </g>
</svg>
</main>
</body>
</html>
```